Brightfold Partners Website

Brightfold Partners (BP) provide Analytics & Enterprise Performance Management (EPM) advisory & consultancy services. We are passionate about data and making a difference for our clients by working in partnership with them, helping them on their journey to becoming an Brightfold Partner. We deliver insights which give our clients a competitive edge and a much deeper understanding of their organisation.

We need a website which shows who we are, what we do and how we do it.

www.brightfold-partners.example is our very basic website at the moment. We want to completely revamp it with a corporate look

```html
<!DOCTYPE html>
<html lang="en">
<head>
<meta charset="UTF-8">
<title>Brightfold Partners — Data Analytics &amp; EPM Consulting</title>
<link href="https://fonts.googleapis.com/css2?family=Montserrat:wght@400;500;600;700&display=swap" rel="stylesheet">
<style>
:root{
  --navy:#2a526b;
  --ink:#1d2b36;
  --text:#3c4650;
  --muted:#6b7680;
  --sky:#e2f3fb;
  --accent:#3d9bd9;
  --line:#d5dbe0;
  --footer:#0d1a27;
  --bar:#2b4d66;
  --badge:#d9dee2;
  --white:#ffffff;
}
*{margin:0;padding:0;box-sizing:border-box}
html,body{width:1200px;height:2816px;overflow:hidden}
body{font-family:'Montserrat',sans-serif;color:var(--text);background:var(--white);position:relative}
.abs{position:absolute}
.backdrop{position:absolute;left:0;top:0}

/* header */
.brand{left:88px;top:22px;display:flex;align-items:center;gap:14px}
.brand-dot{width:58px;height:58px;border-radius:50%;background:var(--navy)}
.brand-name{font-weight:700;font-size:21px;line-height:24px;color:var(--navy);text-transform:uppercase;letter-spacing:.3px}
.topbar{top:14px;left:614px;display:flex;align-items:center;font-size:13px;color:var(--ink);gap:34px}
.topbar span{display:flex;align-items:center;gap:8px}
.social{display:flex;gap:16px;align-items:center}
.social i{display:block;width:11px;height:11px;border-radius:50%;background:var(--navy)}
.nav{top:54px;left:556px;display:flex;gap:39px;font-size:15px;font-weight:500;color:var(--ink)}
.nav .current{color:var(--accent);text-decoration:underline}
.btn-consult{left:967px;top:47px;width:153px;height:33px;background:var(--accent);color:var(--white);font-size:13px;font-weight:700;display:flex;align-items:center;justify-content:center;border-radius:2px}

/* hero */
.hero-title{left:86px;top:228px;font-size:52px;font-weight:700;line-height:60px;color:var(--navy)}
.hero-sub{left:86px;top:350px;font-size:24px;font-weight:600;line-height:38px;color:var(--navy);text-transform:uppercase}

/* welcome */
.mark-big{left:88px;top:642px;width:262px;height:262px;border-radius:50%;background:var(--navy);display:flex;align-items:center;justify-content:center;color:var(--white);font-weight:700;font-size:22px;text-align:center;line-height:30px}
.welcome{left:482px;top:638px;width:460px}
.welcome h3{font-size:25px;font-weight:600;color:var(--navy)}
.welcome h2{font-size:35px;font-weight:600;color:var(--navy);margin-top:6px}
.welcome p{font-size:15px;line-height:24px;margin-top:20px;color:var(--ink)}
.btn-outline{border:2px solid var(--navy);color:var(--navy);font-size:13px;font-weight:600;display:flex;align-items:center;justify-content:center;background:transparent;border-radius:2px}
.welcome .btn-outline{width:129px;height:37px;margin-top:31px}

.section-title{width:1200px;left:0;text-align:center;font-size:36px;font-weight:600;color:var(--navy)}

/* team */
.member{width:238px;height:256px;background:linear-gradient(160deg,#d9d4cf,#8e857c);color:var(--white)}
.member .meta{position:absolute;left:14px;bottom:20px}
.member b{display:block;font-size:16px;font-weight:700}
.member small{display:block;font-size:11px;margin-top:6px}
.arrow-btn{width:30px;height:30px;border:2px solid var(--navy);border-radius:8px;display:flex;align-items:center;justify-content:center}

/* services */
.service{height:337px;color:var(--white)}
.service .meta{position:absolute;left:16px;right:16px;bottom:20px}
.service h4{font-size:19px;font-weight:700}
.service p{font-size:13px;line-height:19px;margin-top:12px;opacity:.85}
.service a{display:block;font-size:13px;margin-top:12px;color:var(--white);text-decoration:none}
.service a.link{color:#6fbfef}

/* inquiry */
.field label{display:block;font-size:13px;color:var(--muted);margin-bottom:8px}
.field .box{width:272px;height:38px;border:1px solid var(--line);background:var(--white);position:relative}
.field .box::before{content:"";position:absolute;left:12px;top:13px;width:10px;height:10px;border:1.5px solid #aab3ba;border-radius:2px}
.field .box.tall{height:118px}
.btn-submit{left:541px;top:2264px;width:118px;height:36px}
.partner-badge{left:420px;top:2368px;width:360px;height:48px;border-radius:4px;background:var(--badge)}

/* footer */
.footer{left:0;top:2488px;width:1200px;height:287px;background:var(--footer)}
.foot-brand{left:94px;top:2600px;display:flex;align-items:center;gap:12px}
.foot-brand .dot{width:56px;height:56px;border-radius:50%;background:var(--white)}
.foot-brand span{color:var(--white);font-weight:700;font-size:16px;line-height:22px;width:110px}
.foot-col h5{font-size:18px;font-weight:600;color:var(--accent);margin-bottom:16px}
.foot-col li{list-style:none;color:var(--white);font-size:15px;line-height:29px}
.foot-col li.current{text-decoration:underline}
.contact-row{display:flex;gap:14px;color:var(--white);font-size:15px;line-height:21px;margin-bottom:14px}
.map{left:824px;top:2558px;width:296px;height:158px;background:linear-gradient(135deg,#f4efe4,#e6edf2);border-radius:3px}
.to-top{left:1128px;top:2728px;width:43px;height:43px;border-radius:50%;background:var(--bar);display:flex;align-items:center;justify-content:center}
.bottom-bar{left:0;top:2775px;width:1200px;height:41px;background:var(--bar);color:var(--white);font-size:15px}
.bottom-bar .copy{position:absolute;left:88px;top:11px}
.bottom-bar .social{position:absolute;right:88px;top:15px;gap:26px}
.bottom-bar .social i{background:var(--white)}
</style>
</head>
<body>

<svg class="backdrop" width="1200" height="2816" viewBox="0 0 1200 2816" aria-hidden="true">
  <path d="M0 575 C120 600 330 720 430 860 C520 990 480 1160 380 1270 C300 1360 120 1400 0 1412 Z" fill="var(--sky)"/>
  <path d="M1200 1700 C1020 1780 760 1880 690 2020 C620 2160 720 2300 900 2380 C1020 2430 1120 2460 1200 2470 Z" fill="var(--sky)"/>
  <path d="M0 2380 C250 2420 600 2440 900 2410 C1050 2395 1150 2420 1200 2460 L1200 2488 L0 2488 Z" fill="var(--sky)" opacity=".6"/>
</svg>

<svg class="abs" style="left:420px;top:80px" width="780" height="562" viewBox="0 0 780 562" role="img" aria-label="City skyscrapers seen from below with rising financial chart lines">
  <defs>
    <linearGradient id="heroFill" x1="0" y1="1" x2="1" y2="0">
      <stop offset="0" stop-color="#2c4f73"/>
      <stop offset=".45" stop-color="#8a7fb0"/>
      <stop offset=".75" stop-color="#e8d7a6"/>
      <stop offset="1" stop-color="#c9d8e6"/>
    </linearGradient>
  </defs>
  <path d="M130 30 C220 0 500 -10 780 10 L780 520 C700 560 600 570 480 520 C360 470 250 410 150 360 C40 300 0 230 10 160 C20 90 70 50 130 30 Z" fill="url(#heroFill)"/>
</svg>

<header>
  <div class="abs brand"><div class="brand-dot"></div><div class="brand-name">Brightfold<br>Partners</div></div>
  <div class="abs topbar">
    <span><svg width="13" height="13" viewBox="0 0 24 24"><path d="M6 3l4 4-2 3c1 3 3 5 6 6l3-2 4 4-3 3C10 21 3 14 3 6z" fill="none" stroke="#3d9bd9" stroke-width="2"/></svg>01 555 0148</span>
    <span><svg width="14" height="11" viewBox="0 0 14 11"><rect x=".5" y=".5" width="13" height="10" fill="none" stroke="#3d9bd9"/><path d="M.5 .5l6.5 6 6.5-6" fill="none" stroke="#3d9bd9"/></svg>info@brightfold-partners.example</span>
    <span class="social"><i></i><i></i><i></i><i></i></span>
  </div>
  <nav class="abs nav"><span class="current">Home</span><span>Services</span><span>About Us</span><span>Contact Us</span></nav>
  <div class="abs btn-consult">CONSULT NOW</div>
</header>

<h1 class="abs hero-title">Brightfold<br>Partners</h1>
<p class="abs hero-sub">Data Analytics &amp;<br>EPM Consulting Services</p>

<div class="abs mark-big">Brightfold<br>Partners</div>
<section class="abs welcome">
  <h3>Welcome to</h3>
  <h2>Brightfold Partners</h2>
  <p>BP are a Data Analytics &amp; EPM company, specialising in the implementation and support of Business Intelligence, EPM and Data Analytics business solutions, both in the Cloud and on-premise.</p>
  <div class="btn-outline">ABOUT US</div>
</section>

<h2 class="abs section-title" style="top:1005px">Who we are</h2>
<div class="abs arrow-btn" style="left:114px;top:1185px"><svg width="14" height="12" viewBox="0 0 14 12"><path d="M13 6H2M6 1L1 6l5 5" fill="none" stroke="#2a526b" stroke-width="2"/></svg></div>
<div class="abs arrow-btn" style="left:1057px;top:1185px"><svg width="14" height="12" viewBox="0 0 14 12"><path d="M1 6h11M8 1l5 5-5 5" fill="none" stroke="#3d9bd9" stroke-width="2"/></svg></div>
<div class="abs member" style="left:219px;top:1081px" role="img" aria-label="Portrait photo of the company president"><div class="meta"><b>Martin Keane</b><small>President at Brightfold Partners</small></div></div>
<div class="abs member" style="left:482px;top:1081px;background:linear-gradient(160deg,#cfcac6,#7d6f66)" role="img" aria-label="Portrait photo of the chief executive"><div class="meta"><b>Aoife Brennan</b><small>CEO @ Brightfold Partners</small></div></div>
<div class="abs member" style="left:744px;top:1081px;background:linear-gradient(160deg,#d7d2cd,#6f5a4c)" role="img" aria-label="Portrait photo of the chief technology officer"><div class="meta"><b>Niamh Costello</b><small>CTO at Brightfold Partners</small></div></div>
<div class="abs btn-outline" style="left:536px;top:1378px;width:128px;height:36px">VIEW ALL</div>

<h2 class="abs section-title" style="top:1505px">What We do</h2>
<div class="abs service" style="left:88px;top:1581px;width:385px;background:linear-gradient(180deg,#8d8378,#3e5d77)" role="img" aria-label="Consultants reviewing plans together at a desk"><div class="meta"><h4>Advise &amp; Architect</h4><p>Helping our customers understand the art of the possible and safeguarding their investments by...</p><a class="link">Read More</a></div></div>
<div class="abs service" style="left:498px;top:1581px;width:299px;background:linear-gradient(180deg,#7c7a76,#23272c)" role="img" aria-label="Project manager presenting to a team in an office"><div class="meta"><h4>Design &amp; Implement</h4><p>Working with the project management team, through each stage of the...</p><a>Read More</a></div></div>
<div class="abs service" style="left:822px;top:1581px;width:298px;background:linear-gradient(180deg,#6e7a84,#1f252b)" role="img" aria-label="Hands on a laptop with gear and chart overlays"><div class="meta"><h4>Optimise &amp; Manage</h4><p>Our Managed Services delivers proactive, on-demand support for EPM...</p><a>Read More</a></div></div>

<h2 class="abs section-title" style="top:2005px">Quick Inquiry</h2>
<div class="abs field" style="left:173px;top:2082px"><label>First Name</label><div class="box"></div></div>
<div class="abs field" style="left:469px;top:2082px"><label>Last Name</label><div class="box"></div></div>
<div class="abs field" style="left:765px;top:2082px"><label>Your Message</label><div class="box tall"></div></div>
<div class="abs field" style="left:173px;top:2163px"><label>Phone Number</label><div class="box"></div></div>
<div class="abs field" style="left:469px;top:2163px"><label>Your Email</label><div class="box"></div></div>
<div class="abs btn-outline btn-submit">SUBMIT</div>
<div class="abs partner-badge" role="img" aria-label="Technology partner badge"></div>

<footer>
  <div class="abs footer"></div>
  <div class="abs foot-brand"><div class="dot"></div><span>Brightfold Partners</span></div>
  <div class="abs foot-col" style="left:307px;top:2560px"><h5>Quick Link</h5><ul><li class="current">Home</li><li>Services</li><li>About Us</li><li>Contact Us</li></ul></div>
  <div class="abs foot-col" style="left:488px;top:2560px">
    <h5>Contatct Info</h5>
    <div class="contact-row"><svg width="14" height="18" viewBox="0 0 14 18"><path d="M7 0a7 7 0 0 0-7 7c0 5 7 11 7 11s7-6 7-11a7 7 0 0 0-7-7z" fill="#3d9bd9"/><circle cx="7" cy="7" r="2.5" fill="#0d1a27"/></svg><span>14 Harbourview Lane,<br>Eastgate, Dublin 4, D04 QX17</span></div>
    <div class="contact-row" style="margin-top:4px"><svg width="14" height="14" viewBox="0 0 24 24"><path d="M6 2l5 5-3 3c1 3 3 5 6 6l3-3 5 5-3 4C9 22 2 15 2 5z" fill="#3d9bd9"/></svg><span>01 555 0148</span></div>
    <div class="contact-row" style="margin-top:4px"><svg width="16" height="12" viewBox="0 0 16 12"><rect width="16" height="12" fill="#3d9bd9"/><path d="M0 0l8 7 8-7" fill="none" stroke="#0d1a27" stroke-width="1.5"/></svg><span>info@brightfold-partners.example</span></div>
  </div>
  <div class="abs map" role="img" aria-label="Street map showing the office location"></div>
  <div class="abs to-top"><svg width="14" height="16" viewBox="0 0 14 16"><path d="M7 15V2M1 7l6-6 6 6" fill="none" stroke="#fff" stroke-width="2.4"/></svg></div>
  <div class="abs bottom-bar"><span class="copy">Copyright © Brightfold Partners. All Rights Reserved</span><span class="social"><i></i><i></i><i></i><i></i></span></div>
</footer>

</body>
</html>
```